Business card Zottelgarten

Business card is for a self-employed dog trainer with own dog school. Name and logo of the dog school are available. Color specifications as well. The design should be classy and minimalist, but also modern. An already existing idea would be: Front: Only the logo Back: Contact data

Font styles to use
Serif
Sans Serif
Other font styles liked:
• Trajan Pro

Colors
f78f20

Requirements
Must have
• Name: Margit Wendler-Rasch Title: Dipl. Dog Trainer Contain my logo Follow my font and color preferences (see files)

```html
<!DOCTYPE html>
<html lang="de">
<head>
<meta charset="utf-8">
<title>Zottelgarten – Business Card</title>
<link rel="stylesheet" href="https://fonts.googleapis.com/css2?family=Cinzel:wght@400;600&family=Crimson+Text:wght@400&display=swap">
<style>
  :root {
    --page: #e9e5e0;
    --card: #75665a;
    --card-shade: rgba(0,0,0,0.18);
    --white: #ffffff;
    --orange: #f78f20;
    --silhouette: #e4ded8;
  }
  * { box-sizing: border-box; margin: 0; padding: 0; }
  html, body { width: 1200px; height: 900px; overflow: hidden; }
  body {
    background: var(--page);
    font-family: "Crimson Text", Georgia, serif;
    color: var(--white);
    position: relative;
  }
  .card {
    position: absolute;
    left: 250px;
    width: 700px;
    height: 400px;
    background: var(--card);
    border-radius: 22px;
    box-shadow: 0 8px 22px var(--card-shade);
    overflow: hidden;
  }
  .card--front { top: 30px; }
  .card--back { top: 470px; }

  /* Front */
  .brand-dot {
    position: absolute;
    left: 50%;
    top: 78px;
    transform: translateX(-50%);
    width: 130px;
    height: 130px;
    border-radius: 50%;
    background: var(--white);
  }
  .front-name {
    position: absolute;
    top: 226px;
    width: 100%;
    text-align: center;
    font-family: "Cinzel", "Times New Roman", serif;
    font-size: 44px;
    font-weight: 400;
    letter-spacing: 2px;
    line-height: 1.2;
  }
  .front-url {
    position: absolute;
    top: 288px;
    width: 100%;
    text-align: center;
    font-family: "Cinzel", "Times New Roman", serif;
    font-size: 12px;
    letter-spacing: 9px;
    color: var(--orange);
    text-transform: uppercase;
  }

  /* Back */
  .back-name {
    position: absolute;
    left: 60px;
    top: 28px;
    font-family: "Cinzel", "Times New Roman", serif;
    font-size: 44px;
    font-weight: 400;
    letter-spacing: 2px;
    line-height: 1.2;
  }
  .back-url {
    position: absolute;
    left: 64px;
    top: 86px;
    font-family: "Cinzel", "Times New Roman", serif;
    font-size: 11px;
    letter-spacing: 10px;
    color: var(--orange);
    text-transform: uppercase;
  }
  .person { position: absolute; left: 60px; top: 126px; }
  .person__name {
    font-family: "Cinzel", "Times New Roman", serif;
    font-weight: 600;
    font-size: 19px;
    letter-spacing: 1px;
    line-height: 26px;
  }
  .person__title { font-size: 18px; line-height: 24px; color: var(--orange); }
  .address { position: absolute; left: 60px; top: 200px; font-size: 18px; line-height: 24px; }
  .contacts { position: absolute; left: 60px; top: 266px; list-style: none; }
  .contacts li { display: flex; align-items: center; font-size: 18px; height: 28px; }
  .contacts svg { width: 20px; height: 20px; margin-right: 10px; flex: none; }
  .illustration {
    position: absolute;
    right: 30px;
    bottom: 0;
    width: 290px;
    height: 270px;
    background: linear-gradient(180deg, var(--silhouette), #f3efeb);
    opacity: 0.9;
  }
</style>
</head>
<body>

<section class="card card--front" aria-label="Card front">
  <div class="brand-dot"></div>
  <h1 class="front-name">Zottelgarten</h1>
  <p class="front-url">www.zottelgarten.ch</p>
</section>

<section class="card card--back" aria-label="Card back">
  <h2 class="back-name">Zottelgarten</h2>
  <p class="back-url">www.zottelgarten.ch</p>

  <div class="person">
    <p class="person__name">Margit Wendler-Rasch</p>
    <p class="person__title">Dipl. Dog Trainer</p>
  </div>

  <p class="address">Postfach 48 Lindenweg 7<br>8840 Einsiedeln</p>

  <ul class="contacts">
    <li>
      <svg viewBox="0 0 20 20" aria-hidden="true">
        <circle cx="10" cy="10" r="9" fill="none" stroke="#f78f20" stroke-width="1.5"/>
        <rect x="7" y="4.5" width="6" height="11" rx="1" fill="none" stroke="#f78f20" stroke-width="1.3"/>
      </svg>(041) 552-3187
    </li>
    <li>
      <svg viewBox="0 0 20 20" aria-hidden="true">
        <circle cx="10" cy="10" r="9" fill="#f78f20"/>
        <rect x="5" y="6.5" width="10" height="7" fill="none" stroke="#75665a" stroke-width="1.2"/>
        <path d="M5 6.5 L10 11 L15 6.5" fill="none" stroke="#75665a" stroke-width="1.2"/>
      </svg>kontakt@zottelgarten.ch
    </li>
    <li>
      <svg viewBox="0 0 20 20" aria-hidden="true">
        <circle cx="10" cy="10" r="9" fill="#f78f20"/>
        <circle cx="10" cy="10" r="5.5" fill="none" stroke="#75665a" stroke-width="1.1"/>
        <ellipse cx="10" cy="10" rx="2.3" ry="5.5" fill="none" stroke="#75665a" stroke-width="1.1"/>
        <line x1="4.5" y1="10" x2="15.5" y2="10" stroke="#75665a" stroke-width="1.1"/>
      </svg>www.zottelgarten-kurse.ch
    </li>
  </ul>

  <div class="illustration" role="img" aria-label="Large white silhouettes of a tall slender dog standing over a small dog"></div>
</section>

</body>
</html>
```